Two documents one design language.

We are a small insurance broker who is committed to being open and transparent as possible with our customers.

For years, we have used plain word documents (see attachments) for our Policy Wording and our Terms of Business.

But now think we can do better and these plain documents are falling behind what our competitors are offering.

So we are now looking for both these documents to be professionally designed using the same design language for both.

We are putting few constraints on the design, but we do have some:
- It must be done in word as the wording can be changed at any time, so we must be able to maintain the documents ourselves.
- Any pictures or graphics you use must be royalty free so we can re-produce with any complications.
- Any pictures or graphics you use must been supplied as part of the package.
- You MUST NOT change any wording or grammar, it's not ours to change, its the insurers wording and HAS to be agreed with them.
- You must not split any any paragraph or bullet point over two pages.
- We are an insurance broker so what ever design you use, must look professional and inspire confidence... I.e. if you read it your thoughts turn to, these people are approachable, know what they are doing and will look after me.
- We specialise in musical instrument insurance, so we are looking for musical theming.

```html
<!DOCTYPE html>
<html lang="en">
<head>
<meta charset="utf-8">
<title>Policy Booklet – Pages 10–19</title>
<link href="https://fonts.googleapis.com/css2?family=Montserrat:wght@800&family=Oswald:wght@300&family=Open+Sans:wght@400;600;700&display=swap" rel="stylesheet">
<style>
:root{
  --board:#4a4a4a;
  --paper:#ffffff;
  --ink:#3c3c3c;
  --rose:#e8889a;
  --rose-deep:#c2405a;
  --tab-grey:#5a5a5a;
  --band-grey:#9a9a9a;
  --band-dark:#111111;
  --rule:#8a8a8a;
  --wave:#e4e4e4;
}
*{box-sizing:border-box;margin:0;padding:0}
html,body{width:1200px;height:4195px;overflow:hidden;background:var(--board)}
body{position:relative;font-family:"Open Sans",sans-serif;color:var(--ink)}
.spread-title{position:absolute;top:40px;left:0;width:1200px;text-align:center;font-family:"Montserrat",sans-serif;font-weight:800;font-size:190px;line-height:1;color:#fff;letter-spacing:-4px}
.page{position:absolute;width:509px;height:721px;background:var(--paper);overflow:hidden}
.page .waves{position:absolute;left:0;right:0;bottom:16px;height:54%;background:linear-gradient(180deg,rgba(255,255,255,0) 0%,var(--wave) 100%)}
.page-tab{position:absolute;top:0;width:38px;height:22px;font-size:10px;font-weight:700;color:#fff;display:flex;align-items:center;justify-content:center}
.page.left .page-tab{left:0;background:var(--tab-grey)}
.page.right .page-tab{right:0;background:var(--rose)}
.brand{position:absolute;top:22px;font-size:8px;line-height:1.05;font-weight:700;color:var(--rose-deep);text-transform:uppercase;letter-spacing:.5px;text-align:center;width:80px}
.page.left .brand{left:82px}
.page.right .brand{left:320px}
.running{position:absolute;top:29px;font-size:6px;letter-spacing:.8px;color:#666;font-weight:600}
.page.left .running{left:196px}
.page.right .running{left:240px;color:#aaa}
.band{position:absolute;left:0;right:0;bottom:0;height:16px;display:flex}
.band span{display:block;height:100%}
.page.left .band .a{width:160px;background:var(--band-grey)}
.page.left .band .b{flex:1;background:var(--rose)}
.page.right .band .a{width:312px;background:var(--rose)}
.page.right .band .b{flex:1;background:var(--band-dark)}
.body{position:absolute;left:24px;right:26px;top:68px;font-size:6px;line-height:1.5;z-index:1}
.page.right .body{left:46px;right:24px}
.body p{margin-bottom:5px}
.body b{font-weight:700}
.h1{font-family:"Oswald",sans-serif;font-weight:300;font-size:24px;line-height:1.05;color:#333;text-transform:uppercase;border-left:5px solid var(--rule);padding-left:8px;margin-bottom:10px}
.h1.mixed{text-transform:none}
.h1.mixed .up{text-transform:uppercase}
.sub{font-weight:700;margin:8px 0 3px}
.ul{text-decoration:underline;font-weight:700;margin:10px 0 4px}
ol.excl{list-style:none}
ol.excl li{display:flex;gap:10px;margin-bottom:2px}
ol.excl li .n{width:14px;flex:none}
.ind{padding-left:14px}
.ind2{padding-left:26px}
.photo{position:absolute;left:62px;top:329px;width:301px;height:374px;background:linear-gradient(160deg,#d9d4cd 0%,#b9ab9c 45%,#5a4a42 100%);z-index:1}
.addr p{margin-bottom:6px}
.link{color:var(--rose-deep);text-decoration:underline}
</style>
</head>
<body>

<div class="spread-title">10-19</div>

<!-- Page 10 -->
<section class="page left" style="left:93px;top:309px">
  <div class="waves" role="img" aria-label="Soft grey flowing line pattern"></div>
  <div class="page-tab">10</div>
  <div class="brand">Hartwell Brooke Insurance</div>
  <div class="running">POLICY BOOKLET</div>
  <div class="body" style="top:60px">
    <div class="h1 mixed"><span class="up">Exclusions</span> (Applicable to the whole policy)</div>
    <p>This insurance does NOT cover:</p>
    <ol class="excl">
      <li><span class="n">1.</span><span>The first £15 of every claim. This is increased to 10% of the value of the instrument damaged whilst entrusted to a <b>FRIEND</b> (i.e. if the instrument is worth £2,500, the excess would be £250) unless the optional On Loan/Hire cover has been purchased.</span></li>
      <li><span class="n">2.</span><span>Faulty Manipulation. Faulty Manipulation occurs when reasonable care and skill is not exercised by <b>YOU</b> or <b>YOUR</b> authorised agent in the normal adjustment and/or regulation of the insured instrument.</span></li>
      <li><span class="n">3.</span><span>Loss or damage caused by wear, tear, gradual deterioration, moth, vermin, scratching or bruising, depreciation in value, contamination or anything that happens gradually.</span></li>
      <li><span class="n">4.</span><span>Loss or damage caused by climatic or atmospheric conditions or extremes of temperature, unless as a direct result of storm, flood, or fire which involved the presence of a naked flame.</span></li>
      <li><span class="n">5.</span><span>Loss or damage caused by any process of repairing, renovating, maintaining or cleaning.</span></li>
      <li><span class="n">6.</span><span>Loss or damage caused by any fault or defect in the design, manufacture, workmanship or materials of the <b>PROPERTY INSURED</b>.</span></li>
      <li><span class="n">7.</span><span>Any loss and/or damage which <b>YOU</b> may suffer by reasons of claims by Third Parties due to <b>YOUR</b> failure to fulfil any contract.</span></li>
      <li><span class="n">8.</span><span>Any item that could be reasonably considered replaceable in the normal course of using the instrument or accessory (e.g. Strings, reeds, Drum heads, etc) unless damaged or lost as a result of an insured event covered under this policy.</span></li>
      <li><span class="n">9.</span><span>Theft protection when the <b>PROPERTY INSURED</b> is on-loan to a third party unless <b>YOU</b> have selected this level of cover, as confirmed on the <b>SCHEDULE</b>, and taken adequate precautions to assess the identity of the person <b>YOU</b> are loaning the instrument to and retained evidence of their identity and address.</span></li>
      <li><span class="n">10.</span><span>Loss or damage to <b>PROPERTY INSURED</b> while left in an unattended vehicle unless –<br>a) the vehicle is fully enclosed (i.e. not a convertible) and the items are placed out of sight within the boot (where practicable);<br>b) all doors, windows and other openings are closed, securely locked and properly fastened;<br>c) <b>YOU</b> have activated the vehicle alarm system and/or immobiliser (if fitted).</span></li>
      <li><span class="n">11.</span><span>Loss or damage caused deliberately by <b>YOU</b>.</span></li>
      <li><span class="n">12.</span><span>Loss or damage to any piece of equipment or working part caused by its own mechanical breakdown or failure, except where the damage results from a clearly identifiable cause originating outside of the appliance or item.</span></li>
      <li><span class="n">13.</span><span>Damage caused by a third party transportation company unless the instrument/accessory is pack in a suitable rigid case designed for such purpose.</span></li>
      <li><span class="n">14.</span><span>Loss caused by the theft of <b>YOUR</b> instrument whilst entrusted to a <b>FRIEND</b>, unless the optional On Loan/Hire cover has been purchased.</span></li>
      <li><span class="n">15.</span><span>Where structure cover has been added to any instrument, the instrument must have been on continuous cover for a minimum period of 24 months, be outside of the manufacturers warranty and be less than 35 years old from the date of manufacture.</span></li>
      <li><span class="n">16.</span><span>Any legal liability to third parties. (Unless Public Liability cover has been selected under this policy and confirmed on the <b>SCHEDULE</b> and then only in relation to the cover provided under such section).</span></li>
      <li><span class="n">17.</span><span><b>WE</b> shall not be deemed to provide cover or be liable to pay any claim or provide and benefit under this policy to the extent that the provisions of such cover, payment or provision of such benefit would expose <b>US</b> to any sanction, prohibition or restriction under United Nations' resolution or the trade or economic sanctions, laws or regulations of the European Union, United Kingdom or United States of America.</span></li>
      <li><span class="n">18.</span><span><b>Asbestos</b><br><b>WE</b> will not indemnify <b>YOU</b> for any damage, loss, cost, expense, or legal liability arising from activities involving asbestos or asbestos-containing material or products, whether direct or indirect. This includes manufacture, mining, processing, distribution, testing, remediation, removal, storage, disposal, sale, use or exposure, regardless of any other contributing cause or event.</span></li>
    </ol>
  </div>
  <div class="band"><span class="a"></span><span class="b"></span></div>
</section>

<!-- Page 11 -->
<section class="page right" style="left:620px;top:309px">
  <div class="waves" role="img" aria-label="Soft grey flowing line pattern"></div>
  <div class="page-tab">11</div>
  <div class="running">2026</div>
  <div class="brand">Hartwell Brooke Insurance</div>
  <div class="body">
    <p><b>WE</b> will not indemnify <b>YOU</b> against any Damage or <b>YOUR</b> legal liability in respect of any loss, cost or expense caused directly or indirectly by any one or more of the following, whether or not acting in any sequence with any other cause: Disease, epidemic or pandemic, (including in all cases any contagious disease that affects animals) or any limitation or prevention of the use of objects because of hazards or potential hazards to human or animal health.</p>
    <p class="sub">20. Cyber and Data Exclusion</p>
    <p class="ind">20.1 Notwithstanding any provision to the contrary within this <b>Policy</b> or any <b>ENDORSEMENT</b> thereto, this Policy excludes any:<br>i) <b>Cyber Loss</b>, unless subject to the provisions of paragraph 2;<br>ii) loss, damage, liability, claim, cost, expense of whatsoever nature directly or indirectly caused by, contributed to by, resulting from, arising out of or in connection with any loss of use, reduction in functionality, repair, replacement, restoration or reproduction of any <b>Data</b>, including any amount pertaining to the value of such <b>Data</b>, unless subject to the provisions of paragraph 3;<br>regardless of any other cause or event contributing concurrently or in any other sequence thereto.</p>
    <p class="ind">20.2 Subject to all the terms, conditions, limitations and exclusions of this <b>Policy</b> or any <b>ENDORSEMENT</b> thereto, this <b>Policy</b> covers physical loss or physical damage to <b>PROPERTY INSURED</b> under this <b>Policy</b> caused by any ensuing fire or explosion which directly results from a <b>Cyber Incident</b>, unless that <b>Cyber Incident</b> is caused by, contributed to by, resulting from, arising out of or in connection with a <b>Cyber Act</b> including, but not limited to, any action taken in controlling, preventing, suppressing or remediating any <b>Cyber Act</b>.</p>
    <p class="ind">20.3 Subject to all the terms, conditions, limitations and exclusions of this <b>Policy</b> or any <b>ENDORSEMENT</b> thereto, should <b>Data Processing Media</b> owned or operated by the <b>Insured</b> suffer physical loss or physical damage insured by this <b>Policy</b>, then this <b>Policy</b> will cover the cost to repair or replace the <b>Data Processing Medium</b> itself plus the costs of copying the <b>Data</b> from back-up or from originals of a previous generation. These costs will not include research and engineering nor any costs of recreating, gathering or assembling the <b>Data</b>. If such media is not repaired, replaced or restored the basis of valuation shall be the cost of the blank <b>Data Processing Media</b>. However, this <b>Policy</b> excludes any amount pertaining to the value of such <b>Data</b>, to <b>YOU</b> or any other party, even if such <b>Data</b> cannot be recreated, gathered or assembled.</p>
    <p class="ind">20.4 In the event any portion of this exclusion is found to be invalid or unenforceable, the remainder shall remain in full force and effect.</p>
    <p class="ind">20.5 This exclusion supersedes and, if in conflict with any other wording in the <b>Policy</b> or any <b>ENDORSEMENT</b> thereto having a bearing on <b>Cyber Loss</b>, <b>Data</b> or <b>Data Processing Media</b>, replaces that wording.</p>
    <p class="sub">21. Nuclear Energy Risks</p>
    <p><b>WE</b> will not indemnify <b>YOU</b> in respect of Nuclear Energy Risks whether such risks are written directly and/or via Pools and/or Associations.<br>For the purpose of this <b>Policy</b>, Nuclear Energy Risks shall be defined as all first party and or third party insurances in respect of:<br>i) nuclear reactors and nuclear power stations or plant;<br>ii) any other <b>PREMISES</b> or facilities whatsoever related to or concerned with:<br>&nbsp;&nbsp;a) the production of nuclear energy or<br>&nbsp;&nbsp;b) the production or storage or handling of nuclear fuel or nuclear waste<br>iii) any other <b>PREMISES</b> or facilities eligible for insurance by any local Nuclear Pool and/or Association.</p>
  </div>
  <div class="band"><span class="a"></span><span class="b"></span></div>
</section>

<!-- Page 12 -->
<section class="page left" style="left:93px;top:1083px">
  <div class="waves" role="img" aria-label="Soft grey flowing line pattern"></div>
  <div class="page-tab">12</div>
  <div class="brand">Hartwell Brooke Insurance</div>
  <div class="running">POLICY BOOKLET</div>
  <div class="body" style="top:92px;left:36px">
    <p class="sub">22. Pollution</p>
    <p class="ind"><b>WE</b> will not indemnify <b>YOU</b> against loss, <b>Damage</b> or expense directly or indirectly caused by or contributed by or arising from <b>Pollution</b>.</p>
    <p class="ind">This exclusion does not apply if such loss or <b>Damage</b> arises as a direct and sole consequence of one or more <b>Defined Peril</b>.</p>
    <p class="sub">23. Pollution (for use for Public Liability and Products Liability)</p>
    <p><b>WE</b> will indemnify <b>YOU</b> in respect of accidental <b>Bodily Injury</b> or accidental loss of or damage to <b>Property</b> caused solely by <b>Pollution</b> which results from a sudden, identifiable, unintended and unexpected incident if that incident takes place in its entirety at a specific and identified time and place during the <b>PERIOD OF INSURANCE</b> provided that:</p>
    <p class="ind">i) all <b>Pollution</b> which arises out of any one incident will be deemed to have occurred at the time that incident takes place;<br>ii) <b>WE</b> will not indemnify <b>YOU</b> against liability in respect of <b>Pollution</b> happening anywhere in the United States of America or Canada or their territories, possessions, dependencies or protectorates; and<br>iii) nothing in these provisos will increase <b>OUR</b> liability to pay more than the limits of <b>Indemnity</b> specified in the <b>SCHEDULE</b> in total in respect of damages costs fees and expenses awarded against <b>YOU</b> during the <b>PERIOD OF INSURANCE</b>.</p>
  </div>
  <div class="band"><span class="a"></span><span class="b"></span></div>
</section>

<!-- Page 13 -->
<section class="page right" style="left:620px;top:1083px">
  <div class="waves" role="img" aria-label="Soft grey flowing line pattern"></div>
  <div class="page-tab">13</div>
  <div class="running">2026</div>
  <div class="brand">Hartwell Brooke Insurance</div>
  <div class="body" style="top:86px;left:16px">
    <p class="sub">24. Radioactivity</p>
    <p><b>WE</b> will not indemnify <b>YOU</b> against loss, <b>Damage</b>, expense or <b>YOUR</b> legal liability directly or indirectly caused by or contributed by or arising from:</p>
    <p class="ind">i) ionising radiation or contamination by radioactivity from any nuclear fuel or from any nuclear waste from the combustion of nuclear fuel;<br>ii) the radioactive, toxic, explosive or other hazardous or contaminating properties of any nuclear installation, reactor or other nuclear assembly or nuclear component thereof;<br>iii) any weapon of war employing atomic or nuclear fission and/or fusion or other like reaction or radioactive force or matter;<br>iv) the radioactive, toxic, explosive or other hazardous or contaminating properties of any radioactive matter. The exclusion in this sub-clause does not extend to radioactive isotopes, other than nuclear fuel, when such isotopes are being prepared, carried, stored, or used for commercial, agricultural, medical, scientific or other similar peaceful purposes;<br>v) any chemical, biological, bio-chemical, or electromagnetic weapon.</p>
    <p class="sub">25. Terrorism</p>
    <p class="ind">i) <b>WE</b> will not indemnify <b>YOU</b> against loss, <b>Damage</b>, cost, or expense or <b>YOUR</b> legal liability directly or indirectly caused by or arising out of <b>Terrorism</b> or any loss, <b>Damage</b>, costs or expenses directly or indirectly caused by or arising out of any action taken in controlling, preventing, suppressing or in any way relating to any act of <b>Terrorism</b> regardless of any other cause contributing concurrently or in any other sequence to the loss.<br>ii) If <b>WE</b> allege that by reason of this exclusion, any loss, <b>Damage</b>, cost or expense or liability is not covered by this <b>Policy</b>, the burden of proving the contrary shall be upon <b>YOU</b>. In the event any portion of this Exclusion is found to be invalid or unenforceable, the remainder shall remain in full force and effect.</p>
  </div>
  <div class="band"><span class="a"></span><span class="b"></span></div>
</section>

<!-- Page 14 -->
<section class="page left" style="left:93px;top:1856px">
  <div class="waves" role="img" aria-label="Soft grey flowing line pattern"></div>
  <div class="page-tab">14</div>
  <div class="brand">Hartwell Brooke Insurance</div>
  <div class="running">POLICY BOOKLET</div>
  <div class="body" style="top:80px;left:36px">
    <p class="sub">26. War</p>
    <p class="ind">i) <b>WE</b> will not indemnify <b>YOU</b> against any <b>Damage</b> or <b>YOUR</b> legal liability in respect of any loss, cost or expense directly or indirectly caused by, happening through or following war, invasion, act of foreign enemy, hostilities (whether war be declared or not), civil war, rebellion, revolution, insurrection or military or usurped power or confiscation or nationalisation or requisition or destruction of or damage to property by or under the order of any government or public or local authority.</p>
    <p class="sub">27. Micro-Organism Exclusion</p>
    <p class="ind">i) <b>WE</b> will not indemnify <b>YOU</b> against any loss <b>Damage</b> claim cost expenses or other sum directly or indirectly arising out of or relating to mould, mildew, fungus, spores or other micro-organism of any type, nature or description including but not limited to any substance whose presence poses an actual or potential threat to human health.</p>
    <p>This Exclusion applies regardless whether there is:</p>
    <p class="ind">i) any physical loss or <b>Damage to Insured Property</b>;<br>ii) any <b>Defined Peril</b> or cause whether or not contributing concurrently or in any sequence;<br>iii) any loss of use occupancy or functionality;<br>iv) any action required including but not limited to repair, replacement, removal, clean-up, abatement, disposal, relocation or steps taken to address medical or legal concerns or to comply with the advice or orders of any competent public or governmental authority or body.</p>
    <p class="ind">This Exclusion replaces and supersedes any provision in this Policy that provides insurance, in whole or in part, for these matters.</p>
    <p class="sub">28. Computer Systems</p>
    <p><b>WE</b> will not indemnify <b>YOU</b> against <b>YOUR</b> legal liability arising out of failure of any computer system, whether or not <b>YOUR Property</b>, to be date or time compliant including failure of any correction, attempted correction, conversion, renovation, rewriting or replacement of any computer system relating to date or time compliance.</p>
    <p class="ul" style="font-weight:600">General Definitions</p>
    <p>The below definitions relate to the exclusions identified in this Appendix (E3). The Sub-Coverholder should refer to the Standard Policy Documentation for a more exhaustive list of definitions.</p>
    <p><b>Cyber Act</b><br>An unauthorised, malicious or criminal act or series of related unauthorised, malicious or criminal acts, regardless of time and place, or the threat or hoax thereof involving access to, processing of, use of or operation of any <b>Computer System</b>.</p>
    <p><b>Cyber Incident</b><br>The words <b>Cyber Incident</b> shall mean:<br>a) any error or omission or series of related errors or omissions involving access to, processing of, use of or operation of any <b>Computer System</b>; or<br>b) any partial or total unavailability or failure or series of related partial or total unavailability or failures to access, process, use or operate any <b>Computer System</b>.</p>
    <p><b>Cyber Loss</b><br>Any loss, damage, liability, claim, cost or expense of whatsoever nature directly or indirectly caused by, contributed to by, resulting from, arising out of or in connection with any <b>Cyber Act</b> or <b>Cyber Incident</b></p>
  </div>
  <div class="band"><span class="a"></span><span class="b"></span></div>
</section>

<!-- Page 15 -->
<section class="page right" style="left:620px;top:1856px">
  <div class="waves" role="img" aria-label="Soft grey flowing line pattern"></div>
  <div class="page-tab">15</div>
  <div class="running">2026</div>
  <div class="brand">Hartwell Brooke Insurance</div>
  <div class="body" style="top:60px;left:30px">
    <p>including, but not limited to, any action taken in controlling, preventing, suppressing or remediating any <b>Cyber Act</b> or <b>Cyber Incident</b>.</p>
    <p><b>Computer System</b><br>The words <b>Computer System</b> shall mean:</p>
    <p class="ind">a) any computer, hardware, software, communications system, electronic device (including, but not limited to, smart phone, laptop, tablet, wearable device), server, cloud or microcontroller including any similar system or any configuration of the aforementioned and including any associated input, output, data storage device, networking equipment or back up facility, owned or operated by the Insured or any other party.</p>
    <p><b>Damage / Damaged</b><br>Accidental tangible physical loss, damage or destruction.</p>
    <p><b>Data</b><br>Information, facts, concepts, code or any other information of any kind that is recorded or transmitted in a form to be used, accessed, processed, transmitted or stored by a <b>Computer System</b>.</p>
    <p><b>Data Processing Media</b><br>Any <b>PROPERTY INSURED</b> by this <b>Policy</b> on which <b>Data</b> can be stored but not the <b>Data</b> itself.</p>
    <p><b>Pollution</b></p>
    <p class="ind">a) Pollution or contamination by naturally occurring or man-made substances, forces, and organisms, including, but not limited to, (i) any actual, threatened, feared or perceived use of any biological, chemical, radioactive or nuclear agent, material or device, whether or not related in any way to any act of <b>Terrorism</b>, and (ii) the deposit of or impairment by dust or soot, chemical precipitation, adulteration or impurification, or any combination of them whether permanent or transitory; and<br>b) all loss, damage or injury directly or indirectly caused by pollution or contamination as stated in a) above.</p>
    <p><b>Terrorism</b><br>Act of terrorism means an act, including but not limited to the use of force or violence and/or the threat of an act of terrorism, of any person or group(s) of persons, whether acting alone or on behalf of or in connection with any organisation(s) or government(s), committed for political, religious, ideological or similar purposes including the intention to influence any government and/or to put the public, or any section of the public, in fear.</p>
  </div>
  <div class="band"><span class="a"></span><span class="b"></span></div>
</section>

<!-- Page 16 -->
<section class="page left" style="left:93px;top:2628px">
  <div class="waves" role="img" aria-label="Soft grey flowing line pattern"></div>
  <div class="page-tab">16</div>
  <div class="brand">Hartwell Brooke Insurance</div>
  <div class="running">POLICY BOOKLET</div>
  <div class="body" style="top:98px;left:46px;right:20px">
    <div class="h1">How to amend<br>your policy</div>
    <p>Should <b>YOU</b> need to amend <b>YOUR</b> policy, please contact Hartwell Brooke Insurance Services by phone, email or letter advising <b>US</b> of the amendments <b>YOU</b> need to make.</p>
    <p>Any amendment may impact the cost of <b>YOUR</b> policy.</p>
    <p>If there is an additional cost for the change <b>YOU</b> will be advised prior to confirming <b>YOU</b> wish to proceed. Please note: the change will not become effective until the additional cost has been received.</p>
    <p>If the change <b>YOU</b> make results in a refund <b>YOU</b> will be advised before confirming the change. Please note, to comply with anti money laundering legislation <b>WE</b> are required to make all refunds by the same method of payment the funds were originally received. In addition <b>WE</b> do not give refunds if the value is below £10.</p>
    <div class="h1" style="margin-top:18px">Renewing<br>your policy</div>
    <p><b>WE</b> will invite <b>YOU</b> to renew <b>YOUR</b> policy with <b>US</b> at least 21 days prior to the end of this policy. At this time <b>WE</b> will send <b>YOU</b> a renewal package which will highlight the cost of renewal along with other crucial information about <b>YOUR</b> new policy.</p>
    <p><b>WE</b> strongly encourage <b>YOU</b> to read the renewal package thoroughly, paying close attention to the value of the instruments and accessories as manufacturers frequently increase their prices and if <b>YOU</b> wish to benefit from New for Old cover, it is crucial <b>WE</b> are advised of any change in values to retain the benefit of New for Old cover.</p>
    <p><b>YOUR</b> invitation to renew is sent by post and Email to <b>YOUR</b> registered address and email, it is therefore important to ensure <b>WE</b> have <b>YOUR</b> current contact details at all times.</p>
    <p>In addition <b>WE</b> are conscious of the environmental impact of sending renewal package by post, should <b>YOU</b> wish; <b>WE</b> can mark <b>YOUR</b> policy as paperless, please let <b>US</b> know if <b>YOU</b> would like to take advantage of a paperless policy.</p>
  </div>
  <div class="band"><span class="a"></span><span class="b"></span></div>
</section>

<!-- Page 17 -->
<section class="page right" style="left:620px;top:2628px">
  <div class="waves" role="img" aria-label="Soft grey flowing line pattern"></div>
  <div class="page-tab">17</div>
  <div class="running">2026</div>
  <div class="brand">Hartwell Brooke Insurance</div>
  <div class="body" style="top:98px;left:30px">
    <div class="h1">How to cancel<br>this policy</div>
    <p class="ul">YOUR Cancellation Rights</p>
    <p class="ind"><b>YOU</b> may cancel this insurance within 14 days of the day <b>YOU</b> purchase this insurance or the day on which <b>YOU</b> receive the Policy wording, whichever is the later by contacting Hartwell Brooke Insurance Services.</p>
    <p class="ind" style="margin-top:14px"><b>YOU</b> may also cancel this insurance at any other time by contacting Hartwell Brooke Insurance Services.</p>
    <p class="ind" style="margin-top:14px">If this insurance is cancelled then, provided <b>YOU</b> have not made a claim, <b>YOU</b> will be entitled to a refund of any premium paid, subject to a deduction for any time for which <b>YOU</b> have been covered. This will be calculated on a proportional basis. For example, if <b>YOU</b> have been covered for six (6) months, the deduction for the time <b>YOU</b> have been covered will be half the annual premium.</p>
    <p class="ind" style="margin-top:14px">If <b>YOU</b> cancel this insurance outside the 14 days cooling-off period, there will be an additional charge of £10, to cover the administrative cost of cancelling the policy.</p>
    <p class="ind" style="margin-top:14px">If <b>WE</b> pay any claim, in whole or in part, then no refund of premium will be allowed.</p>
    <p class="ul" style="margin-top:14px">OUR Cancellation Rights</p>
    <p class="ind"><b>WE</b> can cancel this insurance by giving <b>YOU</b> 30 days' notice in writing where there is a valid reason for doing so. <b>WE</b> will refund the part of <b>YOUR</b> premium which applies to the remaining <b>PERIOD OF INSURANCE</b> providing <b>YOU</b> have not made a claim. Hartwell Brooke Insurance Services will send <b>OUR</b> cancellation letter to the address shown on the <b>SCHEDULE</b> and will set out the reason for cancellation in this letter. Valid reasons may include but are not limited to:</p>
    <p class="ind2" style="margin-top:12px">• Where <b>WE</b> have been unable to collect a premium payment and this has not been rectified by <b>YOU</b> within the time period given.</p>
  </div>
  <div class="band"><span class="a"></span><span class="b"></span></div>
</section>

<!-- Page 18 -->
<section class="page left" style="left:93px;top:3399px">
  <div class="waves" role="img" aria-label="Soft grey flowing line pattern"></div>
  <div class="page-tab">18</div>
  <div class="brand">Hartwell Brooke Insurance</div>
  <div class="running">POLICY BOOKLET</div>
  <div class="body" style="top:100px;left:60px;right:40px">
    <p>• Where <b>YOU</b> are required in accordance with the terms of this policy to co-operate with <b>US</b>, or send <b>US</b> information or documentation and <b>YOU</b> fail to do so in a way that materially affects <b>OUR</b> ability to process a claim, or <b>OUR</b> ability to defend <b>OUR</b> interests. In this case, <b>WE</b> may issue a cancellation letter and will cancel <b>YOUR</b> policy if <b>YOU</b> fail to co-operate with <b>US</b> or provide the required information or documentation by the end of the cancellation notice period.</p>
    <p style="margin-top:8px">• Where <b>WE</b> reasonably suspect fraud.</p>
    <p style="margin-top:8px">• Due to the use of threatening or abusive behaviour or language, or intimidation or bullying of staff or suppliers.</p>
  </div>
  <div class="photo" role="img" aria-label="Photograph of a musician at home checking a violin beside a laptop and camera tripod"></div>
  <div class="band"><span class="a"></span><span class="b"></span></div>
</section>

<!-- Page 19 -->
<section class="page right" style="left:620px;top:3399px">
  <div class="waves" role="img" aria-label="Soft grey flowing line pattern"></div>
  <div class="page-tab">19</div>
  <div class="running">2026</div>
  <div class="brand">Hartwell Brooke Insurance</div>
  <div class="body addr" style="top:98px;left:30px">
    <div class="h1">Claims conditions</div>
    <p>1. Please ensure that <b>YOU</b> report all incidents which could give rise to a claim, as soon as <b>YOU</b> become aware of them, by contacting:</p>
    <p style="padding-left:118px">Owen Marsh, of Hartwell Brooke Insurance Services,</p>
    <div class="ind2">
      <p>14 Elm Grove,</p>
      <p>Aldworth Green,</p>
      <p>Tilbury Vale,</p>
      <p>Westshire,</p>
      <p>TV4 2QD</p>
      <p>01632 960 418</p>
      <p class="link">claims@hartwellbrooke.example</p>
      <p>For claims involving Public liability <b>YOU</b> must additionally report your claim information to <b>OUR</b> dedicated claims team, Meridian Claims Services (via Contact details below) as soon as possible, but no later than fourteen (14) days, if a claim for liability is made against <b>YOU</b>, any letter, claim, writ, summons or other legal documents <b>YOU</b> receive.</p>
      <p><b>YOU</b> must not admit liability or offer or agree to settle any claim without <b>OUR</b> written permission.</p>
      <p>Meridian Claims Services Ltd</p>
      <p>Beacon House</p>
      <p>9 Harbour Street</p>
      <p>Northbridge</p>
      <p>Eastshire</p>
      <p>NB3 5LP</p>
      <p>Telephone: 0300 555 0192</p>
      <p>Email: <span class="link">team@meridianclaims.example</span></p>
    </div>
    <p style="margin-top:10px">2. <b>YOU</b> will be advised if <b>YOU</b> need to complete a claim form or produce documentation to support <b>YOUR</b> claim. In certain circumstances, a late notification may result in <b>YOUR</b> claim being rejected. <b>YOU</b> must be able to prove ownership or legal responsibility for the <b>PROPERTY INSURED</b> in the event of a claim. This may take the form of a valuation from a suitably qualified valuer (preferably dated within the last 5 years) or a purchase receipt.</p>
  </div>
  <div class="band"><span class="a"></span><span class="b"></span></div>
</section>

</body>
</html>
```